Baby and Kids e-shop (Russian language is needed)

We need a web design for e-shop of a Russian company based in Moscow. We sell maternity things, baby and kids goods, clothes, toys, furniture, home and decor, etc.
We need the design that will suit to the exhisting logo. It should be simple and comfortable to the consumers. Attractive but not too bright (so that the goods' pictures attract more attention to them instead of the design).
The domain name of the company is quillbeck.ru
Design of the main page should be similar to the idea of lulloday.com All button names of the main page are provided in attached file.
While choosing certain category from the menu, we should see the list of goods to the left and list of brands to the right (example: http://www.krovatka-dom.ru/?welcome).

We need:
- main page
- page of the catalogue
- page of the certain category from the catalogue
- page with a certain good
- cart page
- payment page
- quill beck club page (banner and text)
- registration page (banner, registration form, text)
Updates

Target Market(s)

pregnant women, young moms

Industry/Entity Type

Baby

Requirements
Must have
• The webdesign should be very clear and similar to lulloday.com You can suggest a kind of design similar to kindrelo.de, tappelo.de.
The web design should clear state that it is targeted on kids goods, but it is a family e-shop as well.
Nice to have
• 1) In general the design shall be the same as provided sample we like. The design of a page with a concrete good should have tabs: 1) about this good, 2) payment, 3) delivery and return, 4) review; like this: http://www.harbordressco.com/t-shirts-c4/vornik-classic-h-tee-ridge-t-shirt-p81174
2) we need design of stickers like in shown example above: 5% off (First order) and Free Coupon for X Rubles for every 1000 Rubles spent online
3) instead of Bookmark&share, ask a question, e-mail a friend and add to wish list, we should have "share" (Chatterly, Druzhnet, Svoyakh - short logos, I will send examples), "ask a question", "e-mail a friend" and "add to gift list" (All this information is contained in downloaded files).

```html
<!DOCTYPE html>
<html lang="ru">
<head>
<meta charset="utf-8">
<title>Quill Beck — детский магазин</title>
<link rel="stylesheet" href="https://fonts.googleapis.com/css2?family=PT+Sans:wght@400;700&family=PT+Serif&family=Oswald:wght@400;500&display=swap">
<style>
:root{
  --page:#ffffff;
  --sheet:#efeeee;
  --card:#efecec;
  --card-line:#d9d7d7;
  --frame:#d6dcb8;
  --text:#222;
  --muted:#8a8a8a;
  --price:#e4172b;
  --btn-top:#f5602c;
  --btn-bot:#d8300a;
  --red:#d9231a;
  --black:#111;
  --footer:#e9e9e9;
}
*{box-sizing:border-box;margin:0;padding:0}
html,body{width:1200px;height:1171px;overflow:hidden;background:var(--page)}
body{font-family:"PT Sans",sans-serif;color:var(--text);position:relative}
.sheet{position:absolute;left:25px;top:0;width:1148px;height:1138px;background:var(--sheet);
  border-left:1px solid var(--frame);border-right:1px solid var(--frame);border-bottom:2px solid var(--frame)}
.card{position:absolute;width:366px;background:var(--card);border:1px solid var(--card-line)}
.card-top{top:-2px;height:65px}
.card-full{top:75px;height:412px}
.price-bar{position:absolute;left:0;right:0;bottom:0;height:54px;border-top:1px solid var(--card-line);
  display:flex;align-items:center;padding:0 15px 0 16px}
.card-top .price-bar{border-top:1px solid var(--card-line);height:54px}
.was{font-size:16px;color:#333;margin-right:11px}
.now{font-size:22px;color:var(--price)}
.btn-cart{margin-left:auto;width:120px;height:31px;border-radius:5px;border:1px solid #b92a08;
  background:linear-gradient(var(--btn-top),var(--btn-bot));color:#fff;font-size:13px;font-weight:700;
  display:flex;align-items:center;justify-content:center;gap:9px}
.btn-cart svg{width:10px;height:10px}
.title{position:absolute;left:12px;top:9px;font-family:"PT Serif",serif;font-size:22px;line-height:22px;color:#111}
.subtitle{position:absolute;left:12px;top:32px;font-family:"PT Serif",serif;font-size:16px;color:#555}
.discount{position:absolute;right:14px;top:10px;text-align:center;font-family:"PT Sans",sans-serif;font-weight:700;line-height:20px}
.discount .pct{color:#f01818;font-size:21px;display:block}
.discount .word{color:#000;font-size:21px;display:block}
.product-photo{position:absolute;left:12px;top:61px;width:342px;height:234px;background:#fff;border:1px solid #cfcfcf;
  display:flex;align-items:center;justify-content:center}
.product-photo .shape{width:130px;height:220px;background:radial-gradient(ellipse at 50% 45%,#4d4f52 0%,#2c2d30 55%,#fff 72%)}
.desc{position:absolute;left:12px;top:311px;width:330px;font-size:12px;line-height:16px;color:#222}
.banner{position:absolute;top:510px;width:366px;height:131px;border:1px solid #ccc}
.banner-club{background:linear-gradient(90deg,#e7e0da,#f3f1f4 60%,#cfc8de)}
.banner-club .tag{position:absolute;left:0;bottom:0;width:210px;height:30px;background:linear-gradient(90deg,#a9cf2e,#7faf16);
  color:#111;font-family:"PT Serif",serif;font-size:18px;padding:4px 9px}
.banner-care{background:linear-gradient(90deg,#7d6a5c,#d9b9a4 50%,#f1dcc9)}
.banner-care .tag{position:absolute;right:0;bottom:0;width:215px;height:30px;background:linear-gradient(90deg,#a9cf2e,#7faf16);
  color:#222;font-family:"PT Serif",serif;font-size:16px;padding:5px 10px}
.banner-care .head{position:absolute;left:8px;top:30px;width:150px;color:#f02a8c;font-family:"PT Sans",sans-serif;font-weight:700;font-size:27px;line-height:25px}
.banner-xmas{background:linear-gradient(90deg,#f4eee8 0%,#e7d8cc 35%,#e4d7cc 100%)}
.banner-xmas .head{position:absolute;left:166px;top:14px;font-family:"PT Serif",serif;font-size:30px;line-height:32px;color:#3a3230}
.banner-xmas .offer{position:absolute;right:12px;top:66px;text-align:right;color:#f0197a;font-weight:700;font-size:23px;line-height:24px}
.about{position:absolute;left:39px;top:660px;width:480px}
.about h2{font-family:"PT Serif",serif;font-weight:400;font-size:21px;color:#333}
.about p{margin-top:14px;font-size:12.4px;line-height:20.6px;color:var(--muted)}
.join{position:absolute;left:550px;top:660px}
.join h3{font-family:"Oswald",sans-serif;font-weight:500;font-size:18px;color:#333}
.email{margin-top:12px;width:306px;height:44px;background:#fff;border:1px solid #d1d1d1;font-size:16px;color:#777;padding:11px 14px}
.signup{margin-top:11px;width:124px;height:36px;background:var(--black);color:#fff;font-family:"Oswald",sans-serif;font-size:20px;
  display:flex;align-items:center;justify-content:center;letter-spacing:1px}
.follow{position:absolute;left:920px;top:665px;width:239px;height:52px;background:var(--red);border:2px solid #fff;
  outline:1px solid #ccc;color:#fff;font-family:"Oswald",sans-serif;font-size:24px;display:flex;align-items:center;justify-content:center}
.social{position:absolute;top:735px;width:54px;text-align:center;font-size:9px;color:#444}
.social .sq{width:42px;height:42px;margin:0 auto 3px;border-radius:6px}
.footer{position:absolute;left:39px;top:846px;width:1120px;height:272px;background:#fff;border:1px solid #d6d6d6;
  box-shadow:0 1px 4px rgba(0,0,0,.15)}
.footer-inner{position:absolute;left:7px;top:7px;right:7px;bottom:7px;background:var(--footer)}
.links{position:absolute;top:28px;list-style:none;font-size:12px;line-height:20.6px;color:#111}
.links li{padding-left:15px;position:relative}
.links li.arrow::before{content:"";position:absolute;left:3px;top:7px;border-left:5px solid var(--price);border-top:3.5px solid transparent;border-bottom:3.5px solid transparent}
.brand{position:absolute;right:22px;top:40px;width:190px;text-align:center}
.brand .mark{display:flex;align-items:center;justify-content:center;gap:10px;font-family:"PT Sans",sans-serif;font-weight:700;font-size:30px;color:#e8432b}
.brand .dot{width:44px;height:44px;border-radius:50%;background:#e8432b}
.brand .url{margin-top:36px;font-family:"PT Serif",serif;font-size:19px;color:#888}
.rule{position:absolute;left:16px;right:16px;top:201px;border-top:1px solid #cfcfcf}
.copy{position:absolute;left:18px;top:224px;font-size:12px;color:#222}
.copy span{margin:0 10px}
</style>
</head>
<body>
<div class="sheet"></div>

<!-- Top row (continuation) -->
<div class="card card-top" style="left:35px"><div class="price-bar"><span class="was">was $ 400</span><span class="now">$200</span><span class="btn-cart"><svg viewBox="0 0 10 10"><rect width="10" height="10" fill="#fff"/><path d="M3 2l4 3-4 3z" fill="#d8300a"/></svg>add in cart</span></div></div>
<div class="card card-top" style="left:416px"><div class="price-bar"><span class="was">was $ 400</span><span class="now">$200</span><span class="btn-cart"><svg viewBox="0 0 10 10"><rect width="10" height="10" fill="#fff"/><path d="M3 2l4 3-4 3z" fill="#d8300a"/></svg>add in cart</span></div></div>
<div class="card card-top" style="left:795px"><div class="price-bar"><span class="was">was $ 400</span><span class="now">$200</span><span class="btn-cart"><svg viewBox="0 0 10 10"><rect width="10" height="10" fill="#fff"/><path d="M3 2l4 3-4 3z" fill="#d8300a"/></svg>add in cart</span></div></div>

<!-- Product cards -->
<div class="card card-full" style="left:35px">
  <div class="title">Trekway Pushchair</div><div class="subtitle">Travel System</div>
  <div class="discount"><span class="pct">50%</span><span class="word">Discount</span></div>
  <div class="product-photo" role="img" aria-label="Dark grey three-wheel pushchair"><div class="shape"></div></div>
  <p class="desc">includes pushcair, infant car seat and Lulloday Weatershield</p>
  <div class="price-bar"><span class="was">was $ 400</span><span class="now">$200</span><span class="btn-cart"><svg viewBox="0 0 10 10"><rect width="10" height="10" fill="#fff"/><path d="M3 2l4 3-4 3z" fill="#d8300a"/></svg>add in cart</span></div>
</div>
<div class="card card-full" style="left:416px">
  <div class="title">Trekway Pushchair</div><div class="subtitle">Travel System</div>
  <div class="discount"><span class="pct">50%</span><span class="word">Discount</span></div>
  <div class="product-photo" role="img" aria-label="Dark grey three-wheel pushchair"><div class="shape"></div></div>
  <p class="desc">includes pushcair, infant car seat and Lulloday Weatershield</p>
  <div class="price-bar"><span class="was">was $ 400</span><span class="now">$200</span><span class="btn-cart"><svg viewBox="0 0 10 10"><rect width="10" height="10" fill="#fff"/><path d="M3 2l4 3-4 3z" fill="#d8300a"/></svg>add in cart</span></div>
</div>
<div class="card card-full" style="left:795px">
  <div class="title">Trekway Pushchair</div><div class="subtitle">Travel System</div>
  <div class="discount"><span class="pct">50%</span><span class="word">Discount</span></div>
  <div class="product-photo" role="img" aria-label="Dark grey three-wheel pushchair"><div class="shape"></div></div>
  <p class="desc">includes pushcair, infant car seat and Lulloday Weatershield</p>
  <div class="price-bar"><span class="was">was $ 400</span><span class="now">$200</span><span class="btn-cart"><svg viewBox="0 0 10 10"><rect width="10" height="10" fill="#fff"/><path d="M3 2l4 3-4 3z" fill="#d8300a"/></svg>add in cart</span></div>
</div>

<!-- Promo banners -->
<div class="banner banner-club" style="left:35px" role="img" aria-label="Smiling woman holding shopping bags"><div class="tag">Клуб Квилл Бек</div></div>
<div class="banner banner-care" style="left:416px" role="img" aria-label="Mother and baby smiling together"><div class="head">the baby care day</div><div class="tag">click here for more details</div></div>
<div class="banner banner-xmas" style="left:795px" role="img" aria-label="Baby in a Santa hat"><div class="head">Chrtistmas<br>Offer</div><div class="offer">50% off<br>on Baby Wear</div></div>

<!-- About / subscribe / follow -->
<section class="about">
  <h2>Блок текста о продукции магазина</h2>
  <p>Lorem Ipsum is simply dummy text of the printing and typesetting industry. Lorem Ipsum has been the industry's standard dummy text ever since the 1500s, when an unknown printer took a galley of type and scrambled it to make a type specimen book. It has survived not only five centuries.But also the leap into electronic typesetting, remaining essentially unchanged. It was popularised in the 1960s with the release of Letraset sheets containing Lorem Ipsum passages.</p>
</section>
<section class="join">
  <h3>ПРИСОЕДИНЯЙТЕСЬ К НАМ</h3>
  <div class="email">Enter your email id</div>
  <div class="signup">SIGN UP</div>
</section>
<div class="follow">FIND / FOLLOW US</div>
<div class="social" style="left:918px"><div class="sq" style="background:#3b5a98"></div>Chatterly</div>
<div class="social" style="left:980px"><div class="sq" style="background:#4fb8de"></div>Chirpwell</div>
<div class="social" style="left:1043px"><div class="sq" style="background:#1e5aa8"></div>Svoyakh</div>
<div class="social" style="left:1105px"><div class="sq" style="background:#4a6f98"></div>Druzhnet</div>

<!-- Footer -->
<footer class="footer">
  <div class="footer-inner">
    <ul class="links" style="left:19px">
      <li class="arrow">Обратная связь</li><li class="arrow">О нас</li><li class="arrow">Как купить</li><li class="arrow">Доставка и оплата</li><li class="arrow">Партнерам</li><li class="arrow">Наши вакансии</li><li class="arrow">Карта сайта</li>
    </ul>
    <ul class="links" style="left:233px">
      <li class="arrow">Каталоги</li><li class="arrow">Зима 2011-2012</li><li class="arrow">Карнавальные костюмы</li><li class="arrow">Школьная форма</li><li class="arrow">Спорт и дети</li><li class="arrow">Модная мама</li><li>Классные штучки</li>
    </ul>
    <ul class="links" style="left:447px">
      <li class="arrow">Отследить заказ</li><li class="arrow">Сертификаты</li><li class="arrow">Подарки с доставкой</li><li class="arrow">Карта клиента</li><li class="arrow">Клуб Квилл Бек</li><li class="arrow">Статьи и полезные советы</li><li class="arrow">Счетчики</li>
    </ul>
    <div class="brand">
      <div class="mark"><span class="dot"></span>Quill Beck</div>
      <div class="url">www.quillbeck.ru</div>
    </div>
    <div class="rule"></div>
    <p class="copy">© 2011, All Rights Reserved, www.quillbeck.ru,<span></span>Privacy Policy<span>|</span>Terms &amp; Conditions</p>
  </div>
</footer>
</body>
</html>
```